Lumetta small bites needs a website.

I have a small dessert bite catering business creating uniquely crafted small dessert bites made with high quality ingredients focusing on gluten free and vegan options.
I would like a website to show off my creations and provide a way for customers to reach me. I work out of a catering kitchen so would include the address of the kitchen as well as my (555) 014-2278 and email etc.

I already own the “www.lumettasmallbites.example” domain but have not used it yet. I have zero knowledge on website creation and design so need help in design as well as coding. I’m not sure how many pages I need designed. I would like one for the dessert bar / catering focus and one for my tasting boxes. I would like a way to upload new tasting box pictures and information to the website as they come out.

Target Market(s)

Individuals or businesses wanting to buy small bite desserts for weddings, gatherings and events for a dessert bar table. I also am creating monthly / seasonal tasting boxes (holiday, Valentine’s Day, etc) that I’d like to highlight.

Industry/Entity Type

Dessert catering, vegan and gluten free

Coding

Coded - Design and coding required

Number of Pages Required

2 page

Colors
E54698
E96AAD
F1A4CE
F9D9EA
FCEFF6

Requirements
Must have
• Pictures of my desserts and text explaining my process of creating individual flavor profiled desserts for people. I would like it to match the current color scheme and vibe of my logo. Must say that I am a catering company so don’t have a bakery but do have frozen tasting boxes available at the store front of the commercial kitchen that I use.
Nice to have
• I would like the website to have the vibe and colors of my logo but would welcome additional creativity from the designer. Include pink and brown as the main colors

```html
<!DOCTYPE html>
<html lang="en">
<head>
<meta charset="utf-8">
<title>Lumetta small bites</title>
<link href="https://fonts.googleapis.com/css2?family=Playfair+Display:wght@700&family=Montserrat:wght@400;500;600;700&display=swap" rel="stylesheet">
<style>
:root{
  --pink:#E54698;
  --pink-mid:#E96AAD;
  --pink-soft:#F1A4CE;
  --pink-pale:#F9D9EA;
  --pink-mist:#FCEFF6;
  --brown:#7b3d17;
  --brown-deep:#4a2410;
  --ink:#3a2a2a;
  --white:#ffffff;
}
*{box-sizing:border-box;margin:0;padding:0}
html,body{width:677px;height:1200px;overflow:hidden;background:var(--white)}
body{font-family:"Montserrat",sans-serif;color:var(--ink);position:relative}
h1,h2,h3{font-family:"Playfair Display",serif}

/* Header */
.site-nav{position:absolute;top:0;left:160px;width:357px;height:24px;background:var(--pink);display:flex;align-items:center;font-size:6.5px;color:var(--white);font-weight:500;z-index:3}
.site-nav a{color:inherit;text-decoration:none}
.nav-left{display:flex;gap:22px;padding-left:16px;width:150px}
.nav-right{display:flex;gap:30px;margin-left:auto;padding-right:20px}
.nav-left .active{background:var(--white);color:var(--pink);padding:2px 6px;border-radius:2px}
.brand{position:absolute;left:50%;top:0;transform:translateX(-50%);width:70px;height:74px;background:var(--white);border-radius:0 0 35px 35px;display:flex;flex-direction:column;align-items:center;justify-content:center;gap:4px;z-index:4}
.brand-dot{width:24px;height:24px;border-radius:50%;background:var(--pink-pale)}
.brand-name{font-family:"Montserrat",sans-serif;font-weight:700;font-size:10px;color:var(--pink)}

/* Hero */
.hero{position:absolute;top:0;left:0;width:677px;height:372px}
.hero-photo{position:absolute;inset:0;background:radial-gradient(ellipse at 45% 80%,#8a4a2c 0%,#5a2e1c 35%,#b89890 70%,#d8ccc8 100%)}
.hero-copy{position:absolute;top:200px;left:0;width:100%;text-align:center;color:var(--white)}
.hero-copy h1{font-size:30px;letter-spacing:.5px}
.hero-copy p{font-size:11px;margin:8px auto 0;width:380px;line-height:1.35}
.btn{display:inline-block;background:var(--pink);color:var(--white);font-size:7px;font-weight:600;padding:6px 14px;border-radius:12px;text-transform:uppercase;letter-spacing:.3px}
.hero-copy .btn{margin-top:12px}

/* Passion */
.passion{position:absolute;top:372px;left:0;width:677px;height:284px;background:var(--white)}
.passion-text{position:absolute;left:54px;top:66px;width:258px}
.passion-text h2{font-size:13px;color:var(--brown);margin-bottom:8px}
.passion-text p{font-size:5px;line-height:1.5;margin-bottom:6px}
.passion-text .btn{font-size:5px;padding:4px 10px;margin-top:2px}
.passion-photo{position:absolute;left:318px;top:40px;width:304px;height:196px;background:linear-gradient(135deg,#c8b8a8,#6b4a3a 55%,#d9b8c0)}

/* Why choose */
.why{position:absolute;top:656px;left:0;width:677px;height:172px;background:var(--pink-mist);text-align:center}
.section-title{font-size:13px;color:var(--brown);padding-top:20px}
.why-cards{display:flex;gap:16px;justify-content:center;margin-top:18px}
.why-card{width:118px;height:92px;background:var(--pink-pale);padding:12px 10px;text-align:center}
.why-card h3{font-family:"Montserrat",sans-serif;font-size:6px;color:var(--brown);margin:6px 0 4px}
.why-card p{font-size:4.6px;line-height:1.5}
.icon{display:block;margin:0 auto}

/* Signature */
.signature{position:absolute;top:828px;left:0;width:677px;height:110px;background:var(--white)}
.signature .section-title{text-align:center;padding-top:20px}
.sig-cols{display:flex;gap:24px;padding:10px 0 0 64px}
.sig-col{width:160px}
.sig-col h3{font-family:"Montserrat",sans-serif;font-size:6.5px;color:var(--brown);margin-bottom:4px}
.sig-col li{font-size:4.6px;line-height:1.6;list-style:none}

/* Gallery */
.gallery{position:absolute;top:938px;left:0;width:677px;height:160px;background:var(--pink-mist);text-align:center}
.gallery .section-title{color:var(--pink);padding-top:12px}
.gallery-row{display:flex;gap:5px;justify-content:center;margin-top:10px}
.gallery-item{width:63px;height:94px}
.g1{background:linear-gradient(160deg,#e8d8cc,#8a5a3a)}
.g2{background:linear-gradient(160deg,#f0e8e0,#6a3a22)}
.g3{background:linear-gradient(160deg,#d8c8b8,#a0522d)}
.g4{background:linear-gradient(160deg,#b8b0a8,#5a3422)}
.g5{background:linear-gradient(160deg,#e0d0c8,#8c6a5a)}
.g6{background:linear-gradient(160deg,#6a4030,#e07030)}
.g7{background:linear-gradient(160deg,#c8a890,#d86a2a)}

/* Footer */
.contact{position:absolute;top:1098px;left:0;width:677px;height:102px;background:var(--brown);color:var(--white);text-align:center}
.contact h2{font-size:13px;padding-top:14px}
.contact p{font-size:5px;line-height:1.6}
.contact .lead{margin:6px 0 4px}
.contact strong{font-weight:700}
.copyright{position:absolute;bottom:0;left:0;width:100%;height:12px;background:var(--brown-deep);font-size:4.5px;line-height:12px}
</style>
</head>
<body>

<section class="hero">
  <div class="hero-photo" role="img" aria-label="Photograph of brownie dessert bites on a white plate"></div>
  <div class="hero-copy">
    <h1>Uniquely Flavorful Bites</h1>
    <p>Elevate your celebrations with handcrafted vegan and gluten-free mini desserts that taste as beautiful as they look.</p>
    <span class="btn">Discover our tasting boxes</span>
  </div>
</section>

<nav class="site-nav">
  <div class="nav-left"><a class="active" href="#">Home</a><a href="#">Dessert Bar &amp; Catering</a></div>
  <div class="nav-right"><a href="#">Tasting Boxes</a><a href="#">Contact</a></div>
</nav>
<div class="brand"><span class="brand-dot"></span><span class="brand-name">Lumetta</span></div>

<section class="passion">
  <div class="passion-text">
    <h2>Our Passion for Pastry</h2>
    <p>Lumetta small bites began with a simple wish to create small dessert bites that everyone can enjoy. We work from a shared catering kitchen rather than a bakery, crafting each flavor profile by hand using high quality ingredients, with gluten-free and vegan options at the heart of every menu we design for you.</p>
    <p>Frozen tasting boxes are available at the store front of our commercial kitchen. Each box changes with the seasons, from holiday treats to Valentine's Day sweets, so there is always something new to taste, share and bring home for the people you love most.</p>
    <span class="btn">Explore dessert bar catering</span>
  </div>
  <div class="passion-photo" role="img" aria-label="Photograph of chocolate topped mini cheesecakes on a tray"></div>
</section>

<section class="why">
  <h2 class="section-title">Why Choose Lumetta</h2>
  <div class="why-cards">
    <div class="why-card">
      <svg class="icon" width="12" height="12" viewBox="0 0 12 12"><circle cx="6" cy="6" r="5.5" fill="var(--pink)"/><path d="M3.4 6.2l1.8 1.8 3.4-3.6" stroke="#fff" stroke-width="1.2" fill="none"/></svg>
      <h3>Inclusive Indulgence</h3>
      <p>Our desserts are made to suit every guest, with vegan and gluten-free choices on all our menus.</p>
    </div>
    <div class="why-card">
      <svg class="icon" width="12" height="12" viewBox="0 0 12 12"><circle cx="6" cy="6" r="5.5" fill="var(--pink)"/><path d="M6 3l.9 2 2.1.2-1.6 1.4.5 2.1L6 7.6 4.1 8.7l.5-2.1L3 5.2l2.1-.2z" fill="#fff"/></svg>
      <h3>Artistic Presentation</h3>
      <p>Each small bite is styled with care so your dessert table looks as lovely as it tastes.</p>
    </div>
    <div class="why-card">
      <svg class="icon" width="12" height="12" viewBox="0 0 12 12"><circle cx="6" cy="6" r="5.5" fill="var(--pink)"/><path d="M6 9S3 7 3 5a1.5 1.5 0 013-.5A1.5 1.5 0 019 5c0 2-3 4-3 4z" fill="#fff"/></svg>
      <h3>Custom Experiences</h3>
      <p>Work with us to design a flavor menu for weddings, parties and gatherings of any size.</p>
    </div>
  </div>
</section>

<section class="signature">
  <h2 class="section-title">Signature Bites</h2>
  <div class="sig-cols">
    <div class="sig-col">
      <h3>Mini Cheesecakes</h3>
      <ul><li>Creamy vegan cheesecake bites</li><li>Seasonal fruit and berry swirls</li><li>Salted caramel and chocolate tops</li></ul>
    </div>
    <div class="sig-col">
      <h3>Brownies &amp; Cakes</h3>
      <ul><li>Fudgy gluten-free brownie squares</li><li>Layered mini cakes with fillings</li><li>Frosted bites for any celebration</li></ul>
    </div>
    <div class="sig-col">
      <h3>Other Bites</h3>
      <ul><li>Tarts and cookie cups</li><li>Seasonal tasting box treats</li><li>Custom flavor requests</li></ul>
    </div>
  </div>
</section>

<section class="gallery">
  <h2 class="section-title">Sweet Inspiration</h2>
  <div class="gallery-row">
    <div class="gallery-item g1" role="img" aria-label="Photograph of frosted mini cupcakes"></div>
    <div class="gallery-item g2" role="img" aria-label="Photograph of brownie squares"></div>
    <div class="gallery-item g3" role="img" aria-label="Photograph of caramel dessert bites"></div>
    <div class="gallery-item g4" role="img" aria-label="Photograph of chocolate bites on a board"></div>
    <div class="gallery-item g5" role="img" aria-label="Photograph of a dessert table"></div>
    <div class="gallery-item g6" role="img" aria-label="Photograph of pumpkin themed bites"></div>
    <div class="gallery-item g7" role="img" aria-label="Photograph of seasonal tasting box treats"></div>
  </div>
</section>

<footer class="contact">
  <h2>Let's Connect</h2>
  <p class="lead">Ready to plan your dessert bar or order a tasting box? We would love to hear about your event and bring these small bites to your table.</p>
  <p><strong>Email:</strong> hello@lumettasmallbites.example</p>
  <p><strong>Phone:</strong> (555) 014-2278</p>
  <p><strong>Kitchen Address:</strong> 210 Orchard Lane, Kitchen 4, Springfield</p>
  <div class="copyright">© 2024 Lumetta small bites · www.lumettasmallbites.example</div>
</footer>

</body>
</html>
```